Thornwick Estates Managment Ltd website

Need a website To inform people/clients of the services we provide. 5 pages total with a local feel. Bristol, UK. I have logo artwork already is like the look based on
incorporate the artwork attached for theme, feel and colours fonts info etc

To best describe the business have a brief look at www.fernbaylettings.co.uk which is a local firm offering the same services. This is for your ref only and not to be copied.

Target Market(s)

Property Investors/Landlords

Coding

Coded - Design and coding required

Number of Pages Required

5+ page

Colors
0392cd
f68d4d

Requirements
Must have
• local feel. Possibly using some local architecture or historic landmarks etc. This is fexible.
• most also be mobile device compatible
Nice to have
• the membership logos - files attached: KTB, GHW, DVT and safebondhold.co.uk

```html
<!DOCTYPE html>
<html lang="en">
<head>
<meta charset="utf-8">
<title>Thornwick Estates Managment Ltd</title>
<link rel="stylesheet" href="https://fonts.googleapis.com/css2?family=Open+Sans:wght@300;400;600;700&display=swap">
<style>
:root{
  --frame:#e4e4e4;
  --white:#ffffff;
  --teal:#2f6f88;
  --teal-btn:#3b7a92;
  --teal-light:#5a9fb8;
  --teal-dark:#1b4b5e;
  --ink:#2b3034;
  --ink-soft:#4a5358;
  --send:#111111;
}
*{box-sizing:border-box;margin:0;padding:0}
html,body{width:1200px;height:2553px;overflow:hidden}
body{background:var(--frame);font-family:"Open Sans",Arial,sans-serif;color:var(--ink);position:relative}
.page{position:absolute;left:15px;top:15px;width:1170px;height:2521px;background:var(--white);overflow:hidden}

/* header */
.site-header{position:absolute;left:0;top:0;width:100%;height:150px}
.brand{position:absolute;left:27px;top:36px;display:flex;align-items:center;gap:14px}
.brand-mark{width:52px;height:52px;background:var(--teal)}
.brand-name{font-size:25px;font-weight:600;color:var(--teal);line-height:1.12;width:270px}
.main-nav{position:absolute;left:635px;top:60px;display:flex;gap:10px}
.main-nav a{display:block;padding:8px 11px;font-size:14px;font-weight:600;color:#2b2f33;text-decoration:none;text-transform:uppercase;border-radius:3px}
.main-nav a.is-active{background:var(--teal-btn);color:var(--white)}

/* hero */
.hero{position:absolute;left:0;top:150px;width:100%;height:499px}
.hero-photo{position:absolute;inset:0;background:
  radial-gradient(ellipse 420px 180px at 30% 10%,rgba(255,226,150,.95) 0%,rgba(238,178,84,.6) 40%,rgba(238,178,84,0) 100%),
  linear-gradient(180deg,#b88a45 0%,#d9a653 12%,#8c7155 26%,#5b5650 40%,#47423c 58%,#33302c 78%,#26241f 100%)}
.hero-title{position:absolute;left:0;width:100%;top:326px;text-align:center;color:var(--white);font-size:37px;font-weight:300}
.hero-rule{position:absolute;left:296px;width:608px;top:385px;height:1px;background:rgba(255,255,255,.75)}
.hero-tagline{position:absolute;left:0;width:100%;top:398px;text-align:center;color:var(--white);font-size:18.5px;font-weight:600;text-transform:uppercase}

/* about */
.about{position:absolute;left:0;top:649px;width:100%;height:340px;background:linear-gradient(180deg,var(--teal-light) 0%,#2f6d85 55%,var(--teal-dark) 100%);color:var(--white)}
.about h2{position:absolute;left:0;width:100%;top:30px;text-align:center;font-size:28px;font-weight:600}
.about-text{position:absolute;left:58px;top:90px;width:578px;font-size:14px;line-height:22.4px}
.about-video{position:absolute;left:725px;top:92px;width:388px;height:207px;border:4px solid var(--white);box-shadow:0 3px 8px rgba(0,0,0,.35)}
.about-video .video-still{position:absolute;inset:0;background:linear-gradient(100deg,#6f93c8 0%,#a9bfdc 28%,#e8e4da 45%,#f1ede4 70%,#c9c2b4 100%)}
.about-video svg{position:absolute;left:164px;top:74px}

/* service bands */
.service{position:absolute;left:0;width:100%;height:400px;overflow:hidden}
.service-photo{position:absolute;top:0;height:100%}
.service--landlords{top:989px}
.service--tenants{top:1389px}
.service--agencies{top:1789px}
.service--landlords .service-photo{left:0;width:630px;clip-path:polygon(0 0,590px 0,630px 50%,590px 100%,0 100%);background:
  radial-gradient(ellipse 260px 200px at 62% 12%,rgba(120,110,110,.55) 0%,rgba(120,110,110,0) 100%),
  radial-gradient(ellipse 300px 260px at 78% 88%,rgba(40,66,140,.9) 0%,rgba(40,66,140,0) 100%),
  linear-gradient(115deg,#f2f2f2 0%,#dcd8d6 30%,#c9b8ae 48%,#8d8890 68%,#3c4f86 100%)}
.service--tenants .service-photo{left:543px;width:627px;clip-path:polygon(38px 0,100% 0,100% 100%,38px 100%,0 50%);background:
  radial-gradient(ellipse 300px 170px at 45% 60%,rgba(72,96,140,.75) 0%,rgba(72,96,140,0) 100%),
  linear-gradient(180deg,#f4f5f4 0%,#e3e6e6 28%,#b8c0ca 50%,#7d8aa3 66%,#c4a37c 84%,#b99570 100%)}
.service--agencies .service-photo{left:0;width:630px;clip-path:polygon(0 0,590px 0,630px 50%,590px 100%,0 100%);background:
  radial-gradient(ellipse 150px 120px at 48% 38%,rgba(225,225,225,.85) 0%,rgba(225,225,225,0) 100%),
  radial-gradient(ellipse 140px 90px at 46% 66%,rgba(200,160,135,.6) 0%,rgba(200,160,135,0) 100%),
  linear-gradient(110deg,#9a9c9e 0%,#6f7276 35%,#4d5155 65%,#2e3135 100%)}
.service-tab{position:absolute;width:170px;height:119px;background:var(--teal);color:var(--white);text-align:center;font-size:14.5px;font-weight:600;text-transform:uppercase}
.service-tab svg{display:block;margin:24px auto 12px}
.service--landlords .service-tab{left:0;top:140px}
.service--tenants .service-tab{right:0;top:140px}
.service--agencies .service-tab{left:0;top:92px}
.service-copy{position:absolute;top:34px;width:450px}
.service--landlords .service-copy,.service--agencies .service-copy{left:678px}
.service--tenants .service-copy{left:41px}
.service-copy h3{font-size:19.5px;font-weight:600;line-height:27px;color:var(--ink);margin-bottom:18px}
.service-copy p{font-size:14.5px;line-height:22px;color:var(--ink-soft);margin-bottom:22px}
.btn{position:absolute;display:block;width:300px;height:39px;line-height:39px;background:var(--teal-btn);color:var(--white);text-align:center;font-size:16px;font-weight:600;text-transform:uppercase;text-decoration:none;border-radius:3px;box-shadow:0 3px 4px rgba(0,0,0,.25)}
.service--landlords .btn{left:73px;top:296px}
.service--tenants .btn{left:68px;top:232px}
.service--agencies .btn{left:73px;top:252px}

/* contact */
.contact{position:absolute;left:0;top:2189px;width:100%;height:303px;background:linear-gradient(180deg,var(--teal-light) 0%,#2f6d85 55%,var(--teal-dark) 100%);color:var(--white)}
.contact h4{position:absolute;font-size:20px;font-weight:600;top:30px}
.contact-heading{left:67px}
.message-heading{left:497px}
.contact-list{position:absolute;left:67px;top:92px;list-style:none;font-size:15px;font-weight:600;line-height:20px}
.contact-list li{display:flex;gap:13px;position:absolute;left:0;white-space:nowrap}
.contact-list li:nth-child(1){top:0}
.contact-list li:nth-child(2){top:65px}
.contact-list li:nth-child(3){top:108px}
.contact-list svg{flex:none;margin-top:2px}
.social{position:absolute;left:90px;top:253px;display:flex;gap:8px}
.social span{width:15px;height:15px;border-radius:50%;background:var(--white)}
.field{position:absolute;background:var(--white);border-radius:2px;font-size:13px;color:#555;padding:10px 14px;height:37px}
.field--name{left:496px;top:89px;width:300px}
.field--email{left:496px;top:137px;width:300px}
.field--phone{left:496px;top:185px;width:300px}
.field--message{left:805px;top:89px;width:300px;height:85px}
.send{position:absolute;left:805px;top:185px;width:106px;height:37px;background:var(--send);color:var(--white);font-size:13px;font-weight:600;text-align:center;line-height:37px;border-radius:2px}

/* footer */
.site-footer{position:absolute;left:0;top:2492px;width:100%;height:29px;text-align:center;font-size:11px;line-height:29px;color:#444;text-transform:uppercase}
</style>
</head>
<body>
<div class="page">

  <header class="site-header">
    <div class="brand">
      <span class="brand-mark"></span>
      <span class="brand-name">Thornwick Estates Managment Ltd</span>
    </div>
    <nav class="main-nav">
      <a class="is-active" href="#">Home</a>
      <a href="#">About Us</a>
      <a href="#">Landlords</a>
      <a href="#">Agencies</a>
      <a href="#">Contact</a>
    </nav>
  </header>

  <section class="hero">
    <div class="hero-photo" role="img" aria-label="Aerial view of Bristol rooftops and towers at sunset"></div>
    <h1 class="hero-title">Thornwick Estates Managment Ltd</h1>
    <div class="hero-rule"></div>
    <p class="hero-tagline">The ideal solution for landlords, tenants &amp; agencies in Bristol</p>
  </section>

  <section class="about">
    <h2>About Us</h2>
    <p class="about-text">Lorem ipsum dolor sit amet, consectetuer adipiscing elit, sed diam nonummy nibh euismod tincidunt ut laoreet dolore magna aliquam erat volutpat. Ut wisi enim ad minim veniam, quis nostrud exerci tation ullamcorper suscipit lobortis nisl ut aliquip ex ea commodo consequat. Duis autem vel eum iriure dolor in hendrerit in vulputate velit esse molestie consequat, vel illum dolore eu feugiat nulla facilisis at vero eros et accumsan et iusto odio dignissim qui blandit praesent luptatum zzril delenit augue duis dolore te feugait nulla facilisi.</p>
    <div class="about-video">
      <div class="video-still" role="img" aria-label="Video still of a curved Georgian terrace street in Bristol"></div>
      <svg width="52" height="52" viewBox="0 0 52 52" aria-hidden="true"><circle cx="26" cy="26" r="26" fill="rgba(0,0,0,.55)"/><path d="M20 15 L38 26 L20 37 Z" fill="#fff"/></svg>
    </div>
  </section>

  <section class="service service--landlords">
    <div class="service-photo" role="img" aria-label="Hand holding out a set of house keys"></div>
    <div class="service-tab">
      <svg width="64" height="24" viewBox="0 0 64 24" aria-hidden="true"><circle cx="12" cy="12" r="10" fill="#fff"/><circle cx="12" cy="12" r="4" fill="var(--teal)"/><rect x="20" y="9" width="40" height="6" fill="#fff"/><rect x="44" y="15" width="5" height="6" fill="#fff"/><rect x="53" y="15" width="5" height="8" fill="#fff"/></svg>
      For Landlords
    </div>
    <div class="service-copy">
      <h3>Guaranteed fixed rent – No bills, no voids, no maintenance, no hassle!</h3>
      <p>The process for landlords is simple. Instead of signing an agreement with a tenant, you sign a management contract with Thornwick Estates Managment Ltd. You don’t need to do anything else. This contract will last for a minimum of two years – but it could be several more if you wish to guarantee your rental payments for longer.</p>
      <p>We will then manage the property and tenants ourselves – you don’t need to lift a finger.</p>
      <a class="btn" href="#">More on for landlords</a>
    </div>
  </section>

  <section class="service service--tenants">
    <div class="service-photo" role="img" aria-label="Young couple sitting among moving boxes in a bright living room"></div>
    <div class="service-tab">
      <svg width="46" height="44" viewBox="0 0 46 44" aria-hidden="true" fill="none" stroke="#fff" stroke-width="3" stroke-linejoin="round"><path d="M6 20 L23 5 L40 20"/><path d="M11 16 V30 H35 V16"/><path d="M3 40 H18 L28 34"/></svg>
      For Tenants
    </div>
    <div class="service-copy">
      <h3>Bills included, modern furniture, very fast broadband, like minded tenants</h3>
      <p>Companies or professional tenants who are interested in accommodation should use the contact button below.</p>
      <p>We are able to provide both short and long term tenancies, and may be able to find homes in your area if we do not currently have any availability.</p>
      <a class="btn" href="#">More on for tenants</a>
    </div>
  </section>

  <section class="service service--agencies">
    <div class="service-photo" role="img" aria-label="Businessman holding a small model house on his palm"></div>
    <div class="service-tab">
      <svg width="56" height="40" viewBox="0 0 56 40" aria-hidden="true" fill="none" stroke="#fff" stroke-width="3" stroke-linejoin="round" stroke-linecap="round"><path d="M3 12 L14 6 L24 10"/><path d="M53 12 L42 6 L30 12 L22 18 L26 22 L34 17"/><path d="M8 16 L24 32 L30 30 L46 16"/><path d="M20 28 L24 24"/><path d="M26 32 L30 27"/></svg>
      For Agencies
    </div>
    <div class="service-copy">
      <h3>5% Guaranteed commission, repeat business, no hassle!</h3>
      <p>Thornwick Estates Managment Ltd is a unique property investment company, operating on multiple levels and is always looking for committed, integral and professional affiliates to help us deliver our service.</p>
      <p>Our aim is to provide quality accommodation to professional tenants with minimal hassle for their landlords.</p>
      <a class="btn" href="#">More on for agencies</a>
    </div>
  </section>

  <section class="contact">
    <h4 class="contact-heading">Contact</h4>
    <ul class="contact-list">
      <li><svg width="14" height="18" viewBox="0 0 14 18" aria-hidden="true"><path d="M7 0 C3 0 0 3 0 7 C0 12 7 18 7 18 C7 18 14 12 14 7 C14 3 11 0 7 0 Z" fill="#fff"/><circle cx="7" cy="7" r="2.5" fill="#2f6d85"/></svg><span>14 Harlow Rd, Old Market<br>Bristol, BS2 9QX</span></li>
      <li><svg width="18" height="16" viewBox="0 0 18 16" aria-hidden="true"><path d="M1 4 C1 1 17 1 17 4 L17 6 L13 6 L13 4 L5 4 L5 6 L1 6 Z" fill="#fff"/><rect x="3" y="7" width="12" height="8" rx="1" fill="#fff"/></svg><span>0117 496 0321</span></li>
      <li><svg width="18" height="14" viewBox="0 0 18 14" aria-hidden="true"><rect x="0" y="0" width="18" height="14" fill="#fff"/><path d="M0 0 L9 8 L18 0" fill="none" stroke="#2f6d85" stroke-width="1.5"/></svg><span>info@thornwickestates.co.uk</span></li>
    </ul>
    <div class="social"><span></span><span></span></div>

    <h4 class="message-heading">Send a Message</h4>
    <div class="field field--name">Name</div>
    <div class="field field--email">Email</div>
    <div class="field field--phone">Phone</div>
    <div class="field field--message">Message</div>
    <div class="send">SEND</div>
  </section>

  <footer class="site-footer">Copyright © 2016 Thornwick Estates Managment Ltd. All rights reserved.</footer>

</div>
</body>
</html>
```